Landlord Handbook for real estate agency clients

We are a boutique Real Estate Agency that specializes in Property Management (Rentals) Located on Sydney's Northern Beaches.

We are putting together a property owners handbook that informs them about being a landlord, setting up their property for rent, local legislation on leasing properties, the services we offer and what makes us a great choice to manage their property.
Ultimately this is designed to answer new landlords FAQs and sell our agency as the best choice for them.

We want this handbook to be simple, clear and styled to match our existing website. wwww.keystonehavenrealty.com.au

We have supplied some images, screen shots of our Landlord Portal service offered. All words and index are provided in the word.doc
The services we want to feature are:
Our Landlord Portal
Our Service Guarantee
Quality Tenant Database
6 Month Property Reports

I would like the brochure to be around 16-20 A4 pages with some of the images provided and/or any other images you would like to add.

An example of a similar owners handbook can be found here: http://www.vexor.com.au/marlow_tebbit_poh/
But I would like something a little more modern and matched to our website design.

I would like a print ready PDF version of document as well as an editable Photoshop copy and AI copy.

Thank you and I look forward t your designs!
Gus.

Target Market(s)

30-65YO Men and women that own investment properties on Sydney's Northern Beaches

Industry/Entity Type

Real Estate

Font styles to use
Serif

Requirements
Must have
• Must use one of the Town house images provided on the front cover to match our website www.keystonehavenrealty.com.au
• Index of details at the start.
• Use one or all of our screen shot images of the Landlord Portal to promote this feature within the landlord portal description in content.
Should not have
• Any images of foreign currency, landscapes or houses. We are based in Sydney Australia on the beach so we want to keep it local and use Australian images, currency, landscapes and houses.

```html
<!DOCTYPE html>
<html lang="en">
<head>
<meta charset="utf-8">
<title>Keystone Haven Realty – Landlord Handbook Covers</title>
<link href="https://fonts.googleapis.com/css2?family=Lato:wght@400;700;900&display=swap" rel="stylesheet">
<style>
  :root {
    --teal: #1aa6b0;
    --teal-dark: #117c86;
    --teal-light: #2fc1c9;
    --ink: #1b1b1b;
    --paper: #ffffff;
    --paper-grey: #eeeeee;
    --backdrop: #d9d6d2;
    --frame: #2b2b2b;
  }
  * { box-sizing: border-box; margin: 0; padding: 0; }
  html, body { width: 1200px; height: 848px; overflow: hidden; }
  body {
    background: var(--backdrop);
    font-family: "Lato", Arial, sans-serif;
    color: var(--ink);
    position: relative;
  }
  .page {
    position: absolute;
    top: 40px;
    width: 542px;
    height: 766px;
    overflow: hidden;
    background: var(--paper);
    box-shadow: 0 6px 18px rgba(0,0,0,.25);
  }
  .page--front { left: 40px; }
  .page--back {
    left: 618px;
    background: linear-gradient(180deg, #ffffff 0%, var(--paper-grey) 55%, #f7f7f7 100%);
  }
  .page svg.art { position: absolute; inset: 0; width: 542px; height: 766px; }

  /* Front cover */
  .cover-title {
    position: absolute;
    left: 60px; top: 48px;
    width: 416px; height: 58px;
    border: 1px solid var(--ink);
    text-align: center;
  }
  .cover-title__top {
    position: absolute; left: 0; right: 0; top: -14px;
    font-size: 26px; font-weight: 400; letter-spacing: .5px;
    line-height: 28px;
  }
  .cover-title__top span { background: #fbfdfe; padding: 0 2px; }
  .cover-title__main {
    position: absolute; left: 0; right: 0; top: 20px;
    font-size: 33px; font-weight: 900; color: var(--teal);
    line-height: 34px;
    display: flex; align-items: center; justify-content: center; gap: 8px;
  }
  .cover-title__main::before,
  .cover-title__main::after {
    content: ""; width: 62px; height: 5px;
    border-top: 1px solid var(--ink); border-bottom: 1px solid var(--ink);
  }
  .brand-name {
    position: absolute;
    font-weight: 900;
    color: var(--ink);
    white-space: nowrap;
    letter-spacing: -.3px;
  }
  .page--front .brand-name { right: 26px; top: 632px; font-size: 31px; }
  .cover-url {
    position: absolute; right: 46px; top: 739px;
    color: #fff; font-size: 12.5px; font-weight: 700;
    letter-spacing: 2.6px; font-style: italic;
  }

  /* Back cover */
  .page--back .brand-name { left: 0; right: 0; text-align: center; top: 158px; font-size: 24px; }
  .contact-box {
    position: absolute;
    left: 91px; top: 498px; width: 371px; height: 72px;
    border: 1px solid #777;
    text-align: center;
    padding-top: 14px;
  }
  .contact-box__address { font-size: 14px; line-height: 19px; }
  .contact-box__email { font-size: 14px; line-height: 19px; color: var(--teal); }
  .contact-box__email b { color: var(--teal-dark); font-weight: 700; }
  .contact-box__web { font-size: 10px; font-weight: 700; letter-spacing: 1px; line-height: 16px; }
  .feature-photo {
    position: absolute;
    left: 110px; top: 246px; width: 334px; height: 257px;
    border: 6px solid var(--frame);
    background: linear-gradient(180deg, #4d9be0 0%, #9fcaf0 38%, #2f8fb2 52%, #5f8a4f 60%, #c9c6bf 72%, #34c4e4 84%, #1fa6cf 100%);
  }
</style>
</head>
<body>

  <section class="page page--front">
    <svg class="art" viewBox="0 0 542 766" aria-hidden="false">
      <defs>
        <linearGradient id="townhouseTones" x1="0" y1="0" x2="0" y2="1">
          <stop offset="0" stop-color="#ffffff"/>
          <stop offset=".12" stop-color="#e8f3f8"/>
          <stop offset=".22" stop-color="#8fc3dc"/>
          <stop offset=".34" stop-color="#3b4548"/>
          <stop offset=".52" stop-color="#6f7a72"/>
          <stop offset=".66" stop-color="#3f7a3a"/>
          <stop offset=".85" stop-color="#2f5e2a"/>
          <stop offset="1" stop-color="#28502a"/>
        </linearGradient>
      </defs>
      <rect role="img" aria-label="Photo of modern terraced townhouses above landscaped garden stairs" x="0" y="0" width="542" height="766" fill="url(#townhouseTones)"/>
      <polygon points="0,690 268,530 348,572 462,452 542,488 542,766 0,766" fill="var(--teal-light)"/>
      <polygon points="0,700 268,542 348,584 462,466 542,504 542,766 0,766" fill="var(--teal-dark)"/>
      <polygon points="0,712 268,556 348,598 462,480 542,520 542,766 0,766" fill="var(--paper)"/>
      <polygon points="160,722 542,722 542,732 150,732" fill="var(--teal-light)"/>
      <polygon points="150,732 542,732 542,766 128,766" fill="var(--teal-dark)"/>
    </svg>

    <div class="cover-title">
      <p class="cover-title__top"><span>PROPERTY MANAGEMENT</span></p>
      <p class="cover-title__main">DONE RIGHT!</p>
    </div>

    <p class="brand-name">KEYSTONE HAVEN REALTY</p>
    <p class="cover-url">www.keystonehavenrealty.com</p>
  </section>

  <section class="page page--back">
    <svg class="art" viewBox="0 0 542 766" aria-hidden="true">
      <rect x="0" y="322" width="542" height="60" fill="var(--teal)"/>
      <rect x="0" y="734" width="542" height="32" fill="var(--teal-dark)"/>
      <polygon points="294,766 366,700 426,736 522,662 542,670 542,766" fill="var(--teal-light)"/>
      <polygon points="314,766 366,716 426,752 522,678 542,686 542,766" fill="var(--paper)"/>
    </svg>

    <p class="brand-name">KEYSTONE HAVEN REALTY</p>

    <div class="contact-box">
      <p class="contact-box__address">PO Box 731, Collaroy, NSW 2097</p>
      <p class="contact-box__email"><b>EMAIL:</b> info@keystonehavenrealty.com.au</p>
      <p class="contact-box__web">www.keystonehavenrealty.com.au</p>
    </div>

    <div class="feature-photo" role="img" aria-label="Photo of a clifftop pool terrace with palm trees overlooking the ocean"></div>
  </section>

</body>
</html>
```